Kettle Ledger Business Card design

We need a stand out business card design for Accounting practice based in Australia specialising in pubs, clubs and hotels. We help venues maximise margins, create time and manage cashflow. One club we have been working with for the last 6 months has increased revenue by 3% and margin by 5% in this time frame. We have a back office outsourced system that costs less than having a full time employee and also allows the venues the added benefit of:<br/>-using the office space to become a revenue generating opportunity. <br/>-a complete system to enhance governance, accountability and efficiency within their operation<br/>-52 weeks cover so no hassle to cover annual/sick .. leave<br/><br/>We would like to see designs that use the colours of our logo (green & blue).
Target Market(s)
Australian Pubs, Clubs & Hotels abookkeeping, accounting and tax services
Industry/Entity Type
Accountant
Contact Information for Business Card
Miriam Oakley CPA
Principal
Accountant Tax Agent
Miriam@KettleLedger-example.com.au
0418693142
www.kettleledger-example.com.au
Accounting / Payroll / Tax / SMSF / Technology
Colors
Designer to choose colors to be used in the design.
Look and feel
Each slider illustrates characteristics of the customer's brand and the style your logo design should communicate.

```html
<!DOCTYPE html>
<html lang="en">
<head>
<meta charset="utf-8">
<title>Kettle Ledger Business Card</title>
<link href="https://fonts.googleapis.com/css2?family=Montserrat:wght@500;600;700&display=swap" rel="stylesheet">
<style>
  :root {
    --brand-blue: #233f8f;
    --brand-green: #0a7040;
    --pattern-blue: #2a4a9e;
    --paper: #ffffff;
    --backdrop: #bbbcc0;
    --ink: #1b1b1b;
  }
  * { margin: 0; padding: 0; box-sizing: border-box; }
  html, body {
    width: 1200px; height: 1200px; overflow: hidden;
    background: var(--backdrop);
    font-family: "Montserrat", Arial, sans-serif;
  }
  .canvas { position: relative; width: 1200px; height: 1200px; }

  .card { position: absolute; left: 197px; width: 805px; height: 460px; overflow: hidden; }
  .card-front { top: 103px; background: var(--paper); }
  .card-back { top: 636px; background: var(--brand-blue); }

  .brand-lockup {
    position: absolute; left: 70px; top: 182px; height: 46px;
    display: flex; align-items: center; gap: 14px;
  }
  .brand-dot { width: 26px; height: 26px; border-radius: 50%; background: var(--brand-green); flex: none; }
  .brand-name { font-weight: 700; font-size: 36px; line-height: 1; color: var(--brand-blue); letter-spacing: -0.5px; white-space: nowrap; }

  .divider { position: absolute; left: 402px; top: 140px; width: 3px; height: 128px; background: var(--brand-green); }

  .person { position: absolute; left: 450px; top: 138px; }
  .person-name { font-weight: 600; font-size: 25px; color: var(--brand-blue); letter-spacing: 0.3px; line-height: 1; }
  .person-role { margin-top: 10px; font-weight: 600; font-size: 11px; color: var(--ink); }

  .contacts { position: absolute; left: 450px; top: 208px; list-style: none; }
  .contact { display: flex; align-items: center; height: 20px; }
  .contact:nth-child(3) { margin-top: 2px; }
  .contact-icon { width: 13px; height: 13px; margin-right: 13px; fill: var(--brand-blue); flex: none; }
  .contact-text { font-weight: 600; font-size: 11px; letter-spacing: 1.1px; color: var(--ink); white-space: nowrap; }
  .contact-phone .contact-text { letter-spacing: 2.6px; }

  .rule-green { position: absolute; left: 0; top: 428px; width: 805px; height: 4px; background: var(--brand-green); }
  .tab-shape { position: absolute; left: 217px; top: 410px; }
  .tab-label {
    position: absolute; left: 240px; top: 411px; width: 323px; text-align: center;
    font-weight: 600; font-size: 11px; letter-spacing: 5px; color: var(--paper); line-height: 19px;
  }
  .services-band {
    position: absolute; left: 0; top: 435px; width: 805px; height: 25px;
    background: var(--brand-blue); color: var(--paper);
    font-weight: 600; font-size: 11.5px; letter-spacing: 1.2px;
    display: flex; align-items: center; justify-content: center;
  }

  .back-pattern {
    position: absolute; inset: 0;
    background: linear-gradient(135deg, var(--brand-blue), var(--pattern-blue) 50%, var(--brand-blue));
  }
  .back-brand {
    position: absolute; left: 600px; top: 322px;
    display: flex; align-items: center; gap: 10px;
  }
  .back-brand .brand-dot { width: 18px; height: 18px; }
  .back-brand .brand-name { font-size: 20px; color: var(--paper); }
</style>
</head>
<body>
<main class="canvas">

  <section class="card card-front" aria-label="Business card front">
    <div class="brand-lockup">
      <span class="brand-dot" aria-hidden="true"></span>
      <span class="brand-name">Kettle Ledger</span>
    </div>

    <div class="divider" aria-hidden="true"></div>

    <div class="person">
      <h1 class="person-name">Miriam Oakley CPA</h1>
      <p class="person-role">Principal</p>
    </div>

    <ul class="contacts">
      <li class="contact contact-phone">
        <svg class="contact-icon" viewBox="0 0 24 24" aria-hidden="true"><path d="M6.6 10.8a15.1 15.1 0 0 0 6.6 6.6l2.2-2.2c.3-.3.7-.4 1-.2 1.1.4 2.3.6 3.6.6.6 0 1 .4 1 1V20c0 .6-.4 1-1 1A17 17 0 0 1 3 4c0-.6.4-1 1-1h3.5c.6 0 1 .4 1 1 0 1.3.2 2.5.6 3.6.1.3 0 .7-.2 1z"/></svg>
        <span class="contact-text">0418693142</span>
      </li>
      <li class="contact">
        <svg class="contact-icon" viewBox="0 0 24 24" aria-hidden="true"><path d="M2 5h20v14H2z" fill="none" stroke="#233f8f" stroke-width="2"/><path d="M2 5l10 8 10-8M2 19l7-7M22 19l-7-7" fill="none" stroke="#233f8f" stroke-width="2"/></svg>
        <span class="contact-text">Miriam@KettleLedger-example.com.au</span>
      </li>
      <li class="contact">
        <svg class="contact-icon" viewBox="0 0 24 24" aria-hidden="true"><circle cx="12" cy="12" r="10" fill="none" stroke="#233f8f" stroke-width="2"/><path d="M2 12h20M12 2c3 3 3 17 0 20M12 2c-3 3-3 17 0 20" fill="none" stroke="#233f8f" stroke-width="1.5"/></svg>
        <span class="contact-text">www.kettleledger-example.com.au</span>
      </li>
    </ul>

    <div class="rule-green" aria-hidden="true"></div>
    <svg class="tab-shape" width="372" height="22" viewBox="0 0 372 22" aria-hidden="true">
      <polygon points="0,22 24,0 346,0 372,22" fill="#0a7040"/>
    </svg>
    <p class="tab-label">Accountant Tax Agent</p>
    <p class="services-band">Accounting/Payroll/Tax/SMSF/Technology</p>
  </section>

  <section class="card card-back" aria-label="Business card back">
    <div class="back-pattern" role="img" aria-label="Repeating pattern of outlined hop cones in a lighter blue"></div>
    <div class="back-brand">
      <span class="brand-dot" aria-hidden="true"></span>
      <span class="brand-name">Kettle Ledger</span>
    </div>
  </section>

</main>
</body>
</html>
```